Real Estate Company Looking for Business Card Designs for 3 Executives

Hello!
Thanks so much for considering our project! We are a real estate investment company located in Edmonton, Alberta called Marlbeck Group of Companies. We invest/develop both commercial and residential real estate and are looking to create 3 DOUBLE-SIDED business cards for 3 top executives in the company! (for some reason it won't let us select the double-sided option, but yes, the cards are double sided and would be happy to tip extra)

We have certain guidelines that we want our business cards to for sure follow - the back of the Business card has to be the Black Background Version of the Logo which has already been designed and linked as a file (first file). We want the entire back of the card to simply just be the black background logo. In terms of the front of the card, would like to see a smaller version of the white background logo (linked as the second file) in the top left hand corner - of course, feel free to get creative and we can make revisions together along the way! and Then after that, just text. We want the card to be sharp, clean, easy on the eyes and highly professional looking. We would like the card to include the Full name of the Company (Marlbeck Group of Companies), Name of the Person, Title, Phone, Email. If possible please provide the front part of the card for 3 people:

1) Marlbeck Group of Companies, Lena Okafor, Chief Financial Officer, 780-555-0162, lenaokafor@marlbeckgroup.example

2) Marlbeck Group of Companies, Tobias Okafor, Chief Executive Officer, 780-555-0148, tobiasokafor@marlbeckgroup.example

3) Marlbeck Group of Companies, Rui Dalton, Chief Operations Officer, 587-555-0193, ruidalton@marlbeckgroup.example

Thank you so much for considering our project & we look forward to seeing your designs!

```html
<!DOCTYPE html>
<html lang="en">
<head>
<meta charset="utf-8">
<title>Marlbeck Group of Companies — Business Card</title>
<link rel="stylesheet" href="https://fonts.googleapis.com/css2?family=Montserrat:wght@400;500;700&display=swap">
<style>
  :root {
    --backdrop: #8a8476;
    --card-white: #f7f7f7;
    --card-black: #1b1b1b;
    --ink: #1a1a1a;
    --ink-soft: #2b2b2b;
    --forest-dark: #1c1c1c;
    --forest-mid: #262626;
    --paper: #ffffff;
  }
  * { margin: 0; padding: 0; box-sizing: border-box; }
  html, body {
    width: 1200px; height: 1200px; overflow: hidden;
    background: var(--backdrop);
    font-family: "Montserrat", sans-serif;
  }
  .canvas { position: relative; width: 1200px; height: 1200px; }
  .card {
    position: absolute; left: 323px; width: 555px; height: 317px;
    border-radius: 16px; overflow: hidden;
  }
  .card-front { top: 262px; background: var(--card-white); color: var(--ink); }
  .card-back { top: 621px; background: var(--card-black); color: var(--paper); }

  .person-name {
    position: absolute; left: 47px; top: 82px;
    font-size: 24px; font-weight: 700; letter-spacing: 0.01em;
  }
  .person-title {
    position: absolute; left: 47px; top: 110px;
    font-size: 14.5px; font-weight: 400; color: var(--ink-soft); letter-spacing: 0.02em;
  }
  .divider {
    position: absolute; left: 48px; top: 167px; width: 45px; height: 2px; background: var(--ink);
  }
  .contact-list { position: absolute; left: 47px; top: 212px; list-style: none; }
  .contact-item {
    display: flex; align-items: center; height: 23.5px;
    font-size: 14.5px; font-weight: 400; color: var(--ink-soft); letter-spacing: 0.01em;
  }
  .contact-icon { width: 15px; height: 15px; margin-right: 10px; flex: none; }

  .brand {
    position: absolute; text-align: center; font-weight: 500;
  }
  .brand-front { left: 318px; width: 220px; top: 88px; color: var(--ink); }
  .brand-back { left: 0; width: 555px; top: 108px; color: var(--paper); z-index: 2; }
  .brand-name { display: block; letter-spacing: 0.34em; padding-left: 0.34em; }
  .brand-sub { display: block; letter-spacing: 0.2em; padding-left: 0.2em; margin-top: 10px; }
  .brand-front .brand-name { font-size: 22px; }
  .brand-front .brand-sub { font-size: 8.5px; }
  .brand-back .brand-name { font-size: 34px; }
  .brand-back .brand-sub { font-size: 11px; margin-top: 16px; }

  .accent-block {
    position: absolute; left: 392px; top: 216px; width: 78px; height: 101px; background: var(--card-black);
  }
  .forest-area {
    position: absolute; left: 0; right: 0; bottom: 0; height: 225px;
    background: linear-gradient(to bottom, var(--card-black) 0%, var(--forest-mid) 55%, var(--forest-dark) 100%);
  }
</style>
</head>
<body>
<main class="canvas">
  <section class="card card-front" aria-label="Business card front">
    <h1 class="person-name">Lena Okafor</h1>
    <p class="person-title">Chief Financial Officer</p>
    <div class="divider"></div>
    <ul class="contact-list">
      <li class="contact-item">
        <svg class="contact-icon" viewBox="0 0 16 16" aria-hidden="true"><circle cx="8" cy="8" r="8" fill="#1a1a1a"/><path d="M5.2 4.2l1.3-.3.8 1.9-.9.7c.5 1.1 1.3 1.9 2.4 2.4l.7-.9 1.9.8-.3 1.3c-3.3.1-6-2.6-5.9-5.9z" fill="#fff"/></svg>
        780-555-0162
      </li>
      <li class="contact-item">
        <svg class="contact-icon" viewBox="0 0 16 16" aria-hidden="true"><circle cx="8" cy="8" r="8" fill="#1a1a1a"/><rect x="4" y="5.2" width="8" height="5.6" fill="none" stroke="#fff" stroke-width="0.9"/><path d="M4 5.4l4 3 4-3" fill="none" stroke="#fff" stroke-width="0.9"/></svg>
        lenaokafor@marlbeckgroup.example
      </li>
      <li class="contact-item">
        <svg class="contact-icon" viewBox="0 0 16 16" aria-hidden="true"><circle cx="8" cy="8" r="8" fill="#1a1a1a"/><g fill="none" stroke="#fff" stroke-width="0.8"><circle cx="8" cy="8" r="4.3"/><ellipse cx="8" cy="8" rx="1.9" ry="4.3"/><path d="M3.7 8h8.6M4.4 5.8h7.2M4.4 10.2h7.2"/></g></svg>
        www.marlbeckgroup.example
      </li>
    </ul>
    <div class="brand brand-front">
      <span class="brand-name">MARLBECK</span>
      <span class="brand-sub">GROUP OF COMPANIES</span>
    </div>
    <div class="accent-block"></div>
  </section>

  <section class="card card-back" aria-label="Business card back">
    <div class="forest-area" role="img" aria-label="Faint silhouette of a conifer forest along the lower part of the card"></div>
    <div class="brand brand-back">
      <span class="brand-name">MARLBECK</span>
      <span class="brand-sub">GROUP OF COMPANIES</span>
    </div>
  </section>
</main>
</body>
</html>
```